Saving Lives with Dental Sleep Medicine

Looking for a brochure to market Dental Sleep Medicine educational courses . Whoever wins this bid will be hired to design the rest of our marketing campaign.
Design should be clean, simple with a modern feel. Not busy. Our courses utilize the most modern technology available.
Brochure content is attached, if you can't fit it all that is ok, we can tweak the content later. We are more focused on the look and feel of this design.
This brochure is marketing a 2 day course so there needs to be a spot for date, location, time & cost. As well as a notice of where to register VelmoraLearning.com, info@velmoralearning.com or call 1.800.###.#### and registration fees.
Also need a spot for Dr. Pelloquist's bio (attached). It's too long so just leave as much space as you can and we can amend the content.
Thank you so much. Looking forward to your designs. VelmEd Team :-)
Updates
Hello,
We are hoping for a minimalist design. Not busy. Clean and simple. We can reduce and minimize verbiage as needed. Just looking for layout and design.
Target Market(s)
Dentists
Requirements
Must have
- Clean lines, simple feel, minimalist and modern. Same font as logo. Black, white, gray.
Should not have
- Busy look and feel

```html
<!DOCTYPE html>
<html lang="en">
<head>
<meta charset="utf-8">
<title>Dental Sleep Medicine Course Brochure</title>
<link rel="stylesheet" href="https://fonts.googleapis.com/css2?family=Open+Sans:ital,wght@0,400;0,700;1,400&display=swap">
<style>
  :root {
    --backdrop: #6b6358;
    --paper: #ffffff;
    --left-top: #b89a86;
    --left-mid: #8a5e52;
    --left-bottom: #3a5552;
    --right-top: #4a4440;
    --right-bottom: #2c2a2a;
    --hex-line: #e25a6e;
    --text-dark: #1d1c1c;
    --text-light: #ece8e4;
    --text-soft: #c9c1ba;
  }
  * { box-sizing: border-box; margin: 0; padding: 0; }
  html, body { width: 1200px; height: 880px; overflow: hidden; }
  body {
    background: var(--backdrop);
    font-family: "Open Sans", Arial, sans-serif;
    position: relative;
  }
  .spread {
    position: absolute;
    left: 40px; top: 90px;
    width: 1120px; height: 700px;
    background: var(--paper);
    padding: 10px;
    display: flex;
  }
  .page {
    position: relative;
    width: 550px; height: 680px;
    overflow: hidden;
  }
  .page--bio {
    background: linear-gradient(180deg, var(--left-top) 0%, var(--left-mid) 45%, #5a4f4b 72%, var(--left-bottom) 100%);
  }
  .page--course {
    background: linear-gradient(180deg, var(--right-top) 0%, #3a3533 50%, var(--right-bottom) 100%);
    border-left: 1px solid #d8d8d8;
  }
  .portrait {
    position: absolute;
    left: 0; top: 0;
    width: 280px; height: 420px;
    background: radial-gradient(ellipse at 45% 35%, #cbb3a0 0%, #a68672 45%, rgba(138,94,82,0) 80%);
  }
  .hex-cluster { position: absolute; left: 0; top: 0; }
  .bio-text, .course-text {
    position: absolute;
    font-size: 9.5px;
    line-height: 12.5px;
  }
  .bio-text { color: var(--text-dark); font-style: italic; }
  .bio-text p + p { margin-top: 12px; }
  .bio-intro { left: 250px; top: 240px; width: 185px; }
  .bio-main { left: 30px; top: 400px; width: 500px; }
  .course-text { color: var(--text-light); }
  .course-title { left: 150px; top: 22px; width: 380px; }
  .course-title .label { color: var(--text-soft); font-size: 9px; }
  .course-title h1 { font-size: 10.5px; line-height: 13px; font-weight: 700; }
  .topics { left: 150px; top: 68px; width: 385px; }
  .topics h2, .section-head { font-size: 10px; font-weight: 700; }
  .topics .columns { display: flex; gap: 14px; }
  .topics ul { list-style: none; }
  .topics .col-main { width: 195px; }
  .topics .col-side { width: 175px; }
  li::before { content: "• "; }
  li { padding-left: 8px; text-indent: -8px; }
  .description { left: 30px; top: 252px; width: 505px; }
  .description p + p { margin-top: 12px; }
  .objectives { left: 30px; top: 445px; width: 505px; }
  .objectives ul { list-style: none; }
</style>
</head>
<body>
<div class="spread">

  <section class="page page--bio">
    <div class="portrait" role="img" aria-label="Portrait photo of the smiling course instructor in a suit, toned sepia"></div>

    <svg class="hex-cluster" width="550" height="320" viewBox="0 0 550 320">
      <g stroke="var(--hex-line)" stroke-width="4" fill="none">
        <line x1="327" y1="188" x2="378" y2="228"/>
        <line x1="490" y1="192" x2="470" y2="218"/>
        <line x1="540" y1="105" x2="550" y2="105"/>
        <line x1="501" y1="296" x2="550" y2="310"/>
      </g>
      <polygon role="img" aria-label="Photo of a monitor in a seminar room" points="330,45 310,79.6 270,79.6 250,45 270,10.4 310,10.4" fill="#6f8aa3" stroke="var(--hex-line)" stroke-width="4"/>
      <polygon role="img" aria-label="Photo of dentists seated at a course lecture" points="540,105 490,191.6 390,191.6 340,105 390,18.4 490,18.4" fill="#9a8b7e" stroke="var(--hex-line)" stroke-width="4"/>
      <polygon role="img" aria-label="Photo of participants working at laptops" points="355,140 327.5,187.6 272.5,187.6 245,140 272.5,92.4 327.5,92.4" fill="#7d736b" stroke="var(--hex-line)" stroke-width="4"/>
      <polygon role="img" aria-label="Photo of a hands-on workshop session" points="522,260 501,296.4 459,296.4 438,260 459,223.6 501,223.6" fill="#6b5a55" stroke="var(--hex-line)" stroke-width="4"/>
    </svg>

    <div class="bio-text bio-intro">
      <p>Dr. Pelloquist received his Doctor of Dental Surgery (DDS) Degree and Bachelor of Medical Sciences from Northfield University, Canada. He also earned fellowships from International Guild of Restorative Aesthetics &amp; Meridian Institute for Advanced Dental Studies. He then furthered his education and training by completing a Research Fellowship in the area of "Sleep and Dental Sleep Medicine" at Valdren University Hospital (VUH), in Valdren, Netherlands.</p>
    </div>

    <div class="bio-text bio-main">
      <p>Dr. Pelloquist is a general dentist who maintains a group of private practices in Harlow and Brenton with an interest in Dental Sleep Medicine and TMD Management. He is actively involved in clinical research in Dental Sleep Medicine and his research focuses on developing new technologies to improve treatment outcome predictability and patient selection in Oral Appliance Therapy for patients with OSA (i.e. Obstructive Sleep Apnea) and improving clinical workflow efficiencies, utilizing different digital technologies. He is the recipient of the "2012 &amp; 2015 Clinical Research Award" and "2015 Clinical Excellence Award" from the Society of Dental Sleep Practice (SDSP). He has lectured at numerous meetings such as SDSP Annual Meeting, IGO (International Guild of Orthodontics) Annual Meeting, Interdisciplinary Coastal Dental Sleep Academy Annual Meeting (iCDSA), Lowland Society of Dental Sleep Practice Annual Meeting (LSDS) and many more Sleep meetings across North America and Europe.</p>
      <p>He is the founder and director of Northfield Dental Sleep Study Club and the Clinical Director at The Quiet Night Centre in Canada. He is also the Chief Dental Officer at Aeolin Sleep Technologies, the developer of "Nocteva" Technology. Dr. Pelloquist is a major advocate for the importance of an inter-disciplinary approach to Dental Sleep Medicine which focuses on the collaboration of Sleep Physicians, Sleep Dentists and other healthcare professionals. He has been treating OSA patients for many years and also has trained hundreds of dentists in Dental Sleep Medicine.</p>
    </div>
  </section>

  <section class="page page--course">
    <svg class="hex-cluster" width="150" height="260" viewBox="0 0 150 260">
      <g stroke="var(--hex-line)" stroke-width="4" fill="none">
        <line x1="0" y1="62" x2="8" y2="62"/>
        <line x1="70" y1="115.7" x2="70" y2="136.3"/>
        <line x1="132" y1="62" x2="150" y2="62"/>
        <line x1="101" y1="243.7" x2="120" y2="258"/>
      </g>
      <polygon role="img" aria-label="Photo of attendees networking at a course" points="132,62 101,115.7 39,115.7 8,62 39,8.3 101,8.3" fill="#5e5652" stroke="var(--hex-line)" stroke-width="4"/>
      <polygon role="img" aria-label="Photo of the instructor teaching a group" points="132,190 101,243.7 39,243.7 8,190 39,136.3 101,136.3" fill="#7a6e68" stroke="var(--hex-line)" stroke-width="4"/>
    </svg>

    <div class="course-text course-title">
      <p class="label">Course Title:</p>
      <h1>Sleep &amp; Airway Management in a Dental Clinic; Nocteva Plus System &amp; Fully Digital Workflows for OAT</h1>
    </div>

    <div class="course-text topics">
      <h2>Topics Covered:</h2>
      <div class="columns">
        <ul class="col-main">
          <li>Fundamentals of Sleep &amp; Sleep Disorders</li>
          <li>Understand Obstructive Sleep Apnea (OSA) &amp; Treatment Options</li>
          <li>How to Implement an effective Sleep Screening Protocol in a Dental Clinic</li>
          <li>Sleep Testing</li>
          <li>How to order an appliance for OAT</li>
          <li>Appliance Selection</li>
          <li>Importance of patient selection</li>
          <li>Overview of Nocteva Plus System</li>
          <li>Hands-on workshop for Nocteva Tray Fitting</li>
          <li>Hands-on workshop for Bite-Registration</li>
        </ul>
        <ul class="col-side">
          <li>Technology &amp; Sleep</li>
          <li>Fully Digital Workflow for OAT</li>
          <li>Nocteva Plus Case Studies</li>
          <li>Medical Billing for OAT</li>
          <li>How to maximize the utilization of your Nocteva Plus at your clinic</li>
          <li>Simple and easy to follow clinical workflow</li>
        </ul>
      </div>
    </div>

    <div class="course-text description">
      <p><span class="section-head">Course Description:</span><br>Dental Sleep Medicine (DSM) has been growing rapidly over the past decade. Despite such growth, Oral Appliance Therapy (OAT) could be challenging in terms of predictability and workflow efficiency, resulting in many clinicians being reluctant to incorporate "Sleep &amp; OAT" into their clinics. However, most of these challenges can now be addressed by utilizing available technologies in healthcare industry; resulting in improved and predictable clinical workflows, patient experience, quality of care and access to care.</p>
      <p>This program will review the importance of Sleep &amp; Airway Management in comprehensive inter-disciplinary treatment planning and how airway &amp; sleep disorders, if left untreated, could adversely impact the long-term prognosis of dental treatments. It will also provide a practical step-by-step guide for implementing a simple &amp; predictable "Sleep and Airway Management" program; utilizing easy to implement systems, improved patient communication &amp; education through intraoral scanning, &amp; 3D imaging AND a fully digital workflow for OAT.</p>
    </div>

    <div class="course-text objectives">
      <p class="section-head">Learning Objectives:</p>
      <ul>
        <li>Step by step instruction on how to systematically integrate sleep into your practice</li>
        <li>Why dental clinics should have a comprehensive understanding of sleep &amp; airway disorders, and educate their patients</li>
        <li>How to implement a sleep and airway management program in a dental clinic</li>
        <li>Overview of some of the latest technologies in dentistry and how each could be utilized in Dental Sleep Medicine (DSM)</li>
        <li>How to utilize your Nocteva Plus System effectively in your clinic</li>
        <li>Proper selection of oral appliances for OSA</li>
        <li>Medical Billing for OAT</li>
      </ul>
    </div>
  </section>

</div>
</body>
</html>
```